Animal Horse & Bedding Company Needs a Website Coded & Designed

We need a website for a new animal bedding and feed company that is visually grabbing and vibrant. We would like to see a website that displays trust, quality and confidence. Needs to be responsive and mobile friendly for all browsers and coded for both Android & IOS. SEO is also important.

Joomla or Wordpress – must be both desktop and mobile friendly with fast page load speed. Need the ability to edit ourselves in Wordpress or Joomla.

Full details attached below with some layout and content ideas.

Coding

Coded - Design and coding required

Number of Pages Required

5+ page

Font styles to use
Sans Serif

Requirements
Must have
• Needs to be responsive and mobile friendly for all browsers and coded for both Android & IOS. SEO is also important.

Wordpress – must be both desktop and mobile friendly with fast page load speed. Need the ability to edit ourselves in Wordpress.

Logo Colours:
Dark Brown
CMYK: 50 / 70 / 80 / 70
Pantone: 4625C

Orange
CMYK: 0 / 50 / 100 / 0
Pantone: 144C
Nice to have
• Use picture of building attached and super impose logo on building.

```html
<!DOCTYPE html>
<html lang="en">
<head>
<meta charset="utf-8">
<title>Golden Furrow — Bedding &amp; Feed</title>
<link href="https://fonts.googleapis.com/css2?family=Oswald:wght@300;400&family=Montserrat:wght@400;500;600;700&family=Poppins:wght@500;600&display=swap" rel="stylesheet">
<style>
:root{
  --brown:#3d2314;
  --brown-deep:#331c10;
  --orange:#f7941d;
  --cream:#f8f4ef;
  --text:#3a3a3a;
  --muted:#6b6b6b;
  --white:#ffffff;
  --line:#e3ddd5;
}
*{margin:0;padding:0;box-sizing:border-box}
html,body{width:1200px;height:3968px;overflow:hidden;background:var(--white)}
body{position:relative;font-family:"Montserrat",sans-serif;color:var(--text)}
.abs{position:absolute}
.display{font-family:"Oswald",sans-serif;font-weight:300;letter-spacing:1px}

/* header */
.site-header{position:absolute;left:0;top:0;width:1200px;height:95px;background:var(--white)}
.brand{position:absolute;left:72px;top:18px;display:flex;align-items:center;gap:12px}
.brand-dot{width:44px;height:44px;border-radius:50%;background:var(--orange)}
.brand-name{font-family:"Oswald",sans-serif;font-weight:400;font-size:32px;color:var(--brown);letter-spacing:2px;line-height:1}
.brand-tag{font-family:"Oswald",sans-serif;font-weight:400;font-size:11px;color:var(--orange);letter-spacing:9px;margin-top:4px}
.main-nav{position:absolute;top:34px;left:412px;display:flex;font-size:14px;color:#333;font-weight:500}
.main-nav a{position:absolute;white-space:nowrap;text-decoration:none;color:inherit}
.main-nav .active{font-weight:700}
.main-nav .active::after{content:"";position:absolute;left:10px;right:10px;top:27px;height:2px;background:var(--orange)}
.btn{display:flex;align-items:center;justify-content:center;gap:8px;font-weight:700;font-size:13px;text-decoration:none;letter-spacing:.3px}
.btn-dark{background:var(--brown);color:var(--white)}
.quote-btn{position:absolute;left:963px;top:27px;width:153px;height:39px;border-radius:20px;font-size:12px}

/* hero */
.hero{position:absolute;left:0;top:95px;width:1200px;height:650px}
.hero-photo{position:absolute;inset:0;background:linear-gradient(160deg,#5a6a34 0%,#8c8a4a 35%,#b06a34 60%,#7e6a3c 85%,#b8a060 100%)}
.hero-title{position:absolute;left:62px;top:190px;font-family:"Oswald",sans-serif;font-weight:400;font-size:88px;color:var(--white);letter-spacing:3px;line-height:1}
.hero-sub{position:absolute;left:157px;top:290px;font-family:"Oswald",sans-serif;font-weight:400;font-size:34px;color:var(--white);letter-spacing:12px}
.learn-btn{position:absolute;left:213px;top:348px;width:183px;height:52px;border-radius:26px 0 26px 0;box-shadow:3px 3px 0 var(--orange)}
.dots{position:absolute;left:570px;top:571px;display:flex;gap:8px}
.dots span{width:11px;height:11px;border-radius:50%;background:var(--white)}
.dots span.on{background:var(--orange);border:2px solid var(--white)}
.hero-curve{position:absolute;left:0;bottom:-10px;width:1200px;height:100px}

/* cards */
.card{position:absolute;top:790px;width:320px;height:407px;background:var(--white);box-shadow:0 2px 8px rgba(0,0,0,.12);text-align:center}
.card-photo{height:210px}
.card h3{font-family:"Oswald",sans-serif;font-weight:400;font-size:26px;color:var(--brown);margin-top:22px;letter-spacing:.5px}
.card h3::after{content:"";display:block;width:40px;height:2px;background:var(--orange);margin:8px auto 0}
.card p{font-size:10.5px;line-height:17px;color:var(--muted);padding:18px 42px 0}
.card.featured{background:var(--brown)}
.card.featured h3,.card.featured p{color:var(--white)}

/* features band */
.features{position:absolute;left:0;top:1250px;width:1200px;height:240px;background:var(--cream);border-bottom:1px solid var(--line)}
.feature{position:absolute;top:80px;display:flex;gap:12px}
.feature h4{font-size:16px;font-weight:500;color:var(--brown);line-height:22px;letter-spacing:.5px}
.feature p{font-size:11px;color:var(--muted);line-height:20px;margin-top:6px}
.divider{position:absolute;top:95px;width:1px;height:110px;background:var(--line)}

/* bedding */
.section-title{position:absolute;font-family:"Oswald",sans-serif;font-weight:400;font-size:44px;color:var(--brown);letter-spacing:1px}
.section-title::after{content:"";display:block;width:52px;height:3px;background:var(--orange);margin:6px auto 0}
.bed-photo{position:absolute;left:421px;top:1660px;width:362px;height:362px;border-radius:50%;background:radial-gradient(circle at 50% 40%,#9b5a2e 0%,#a87a4c 45%,#c4a776 75%,#b6a88a 100%)}
.ico{position:absolute;width:76px;height:76px;border-radius:50%;display:flex;align-items:center;justify-content:center}
.ico.o{background:var(--orange)}
.ico.b{background:var(--brown)}
.ico svg{width:38px;height:38px;fill:none;stroke:var(--white);stroke-width:2}
.ico-label{position:absolute;font-size:14px;line-height:19px;font-weight:500;color:#333}
.view-bed{position:absolute;left:505px;top:2262px;width:189px;height:51px;border-radius:26px 0 26px 0}

/* feed */
.feed{position:absolute;left:0;top:2395px;width:1200px;height:620px;background:linear-gradient(100deg,var(--brown) 0%,var(--brown) 48%,#8a4c1c 68%,var(--orange) 100%)}
.feed h2{position:absolute;left:118px;top:100px;font-family:"Oswald",sans-serif;font-weight:400;font-size:42px;color:var(--white);letter-spacing:1px}
.feed-intro{position:absolute;left:120px;top:170px;width:530px;font-size:11.5px;line-height:21px;color:var(--white)}
.feed-item{position:absolute;display:flex;align-items:center;gap:8px;font-family:"Poppins",sans-serif;font-weight:600;font-size:10px;line-height:12px;color:var(--white)}
.feed-item svg{width:32px;height:32px;fill:none;stroke:var(--white);stroke-width:1.6;flex:none}
.view-feed{position:absolute;left:116px;top:475px;width:153px;height:45px;border:2px solid var(--white);border-radius:22px 0 22px 0;color:var(--white)}
.feed-photo-main{position:absolute;left:695px;top:97px;width:405px;height:343px;background:linear-gradient(135deg,#4a5056 0%,#8b6a46 40%,#c27a3f 60%,#5b6a7a 100%)}
.feed-photo-pellets{position:absolute;left:620px;top:327px;width:220px;height:188px;background:linear-gradient(135deg,#8a6a36 0%,#b8954f 50%,#6e5228 100%)}

/* delivery */
.delivery-photo{position:absolute;left:168px;top:3108px;width:364px;height:364px;border-radius:50%;background:radial-gradient(circle at 50% 45%,#8c4a24 0%,#6e7a3c 55%,#93a460 100%)}
.delivery h2{position:absolute;left:615px;top:3148px;font-family:"Oswald",sans-serif;font-weight:400;font-size:40px;color:var(--brown);letter-spacing:1px}
.delivery-rule{position:absolute;left:620px;top:3212px;width:55px;height:3px;background:var(--orange)}
.delivery p{position:absolute;left:621px;width:430px;font-size:12px;line-height:21px;color:var(--muted)}
.contact-btn{position:absolute;left:620px;top:3366px;width:153px;height:46px;border:2px solid var(--brown);border-radius:22px 0 22px 0;color:var(--brown);font-size:12px}

/* footer */
.site-footer{position:absolute;left:0;top:3470px;width:1200px;height:498px}
.footer-bg{position:absolute;inset:0}
.footer-brand{position:absolute;left:100px;top:150px;width:270px;text-align:center}
.footer-brand .dot{width:40px;height:40px;border-radius:50%;background:var(--orange);margin:0 auto 12px}
.footer-brand .name{font-family:"Oswald",sans-serif;font-weight:400;font-size:36px;color:var(--white);letter-spacing:2px;line-height:1}
.footer-brand .tag{font-family:"Oswald",sans-serif;font-size:12px;color:var(--orange);letter-spacing:10px;margin-top:6px}
.socials{position:absolute;left:168px;top:297px;display:flex;gap:6px}
.socials span{width:32px;height:32px;border-radius:50%;background:var(--white)}
.socials span:first-child{background:var(--orange)}
.f-col h5{font-size:14px;font-weight:500;color:var(--white);letter-spacing:.5px;margin-bottom:18px}
.f-col li{list-style:none;font-size:11px;color:var(--white);line-height:26px}
.f-contact li{display:flex;gap:10px;font-size:10px;line-height:26px}
.f-contact svg{width:14px;height:14px;flex:none;margin-top:5px}
.email-field{width:230px;height:36px;border:1px solid #bba797;border-radius:18px;font-size:10px;color:#d8ccc0;padding:0 20px;display:flex;align-items:center}
.subscribe{margin:6px 0 0 6px;width:132px;height:35px;border-radius:18px;background:var(--white);color:var(--brown);font-size:11px}
.copyright{position:absolute;left:0;top:452px;width:1200px;text-align:center;font-size:10px;color:#d8ccc0}
</style>
</head>
<body>

<header class="site-header">
  <div class="brand">
    <span class="brand-dot"></span>
    <div>
      <div class="brand-name">GOLDEN FURROW</div>
      <div class="brand-tag">BEDDING &amp; FEED</div>
    </div>
  </div>
  <nav class="main-nav">
    <a class="active" style="left:0">HOME</a>
    <a style="left:98px">ABOUT</a>
    <a style="left:200px">FEED</a>
    <a style="left:288px">BEDDING</a>
    <a style="left:405px">CONTACT US</a>
  </nav>
  <a class="btn btn-dark quote-btn">REQUEST QUOTE ›</a>
</header>

<section class="hero">
  <div class="hero-photo" role="img" aria-label="Chestnut horse standing in a sunlit meadow of wildflowers"></div>
  <h1 class="hero-title">GOLDEN FURROW</h1>
  <div class="hero-sub">BEDDING &amp; FEED</div>
  <a class="btn btn-dark learn-btn">LEARN MORE ›</a>
  <div class="dots"><span></span><span class="on"></span><span></span></div>
  <svg class="hero-curve" viewBox="0 0 1200 100" preserveAspectRatio="none">
    <path d="M0 42 Q600 150 1200 42 L1200 100 L0 100Z" fill="#fff"/>
    <path d="M0 42 Q600 150 1200 42" fill="none" stroke="#f7941d" stroke-width="4"/>
  </svg>
</section>

<article class="card" style="left:108px">
  <div class="card-photo" role="img" aria-label="Two horses eating hay" style="background:linear-gradient(135deg,#2e2a28,#6a4a30 50%,#c8b68c)"></div>
  <h3>BEST BEDDING &amp; FEED</h3>
  <p>Looking for the best bedding and feed for your horse, livestock or household pet look no further. We use premium locally sourced straw and hay in all of our products and are committed in providing quality products and service.</p>
</article>
<article class="card featured" style="left:445px">
  <div class="card-photo" role="img" aria-label="Woman standing beside a horse in a green field" style="background:linear-gradient(135deg,#6a3a1a,#9a7a3a 50%,#7a8a3a)"></div>
  <h3>ANIMAL DESERVE BEST</h3>
  <p>Your animal deserves the very best in health and comfort to keep them healthy, strong and happy. Our products are designed for horses, livestock (goats, cattle and sheep), small caged animals (rabbits, guinea pigs and more).</p>
</article>
<article class="card" style="left:782px">
  <div class="card-photo" role="img" aria-label="Horse standing on open grassland" style="background:linear-gradient(180deg,#9ab8d8,#b87a40 55%,#a8b860)"></div>
  <h3>OFFER SUPPLY &amp; DELIVERY</h3>
  <p>Golden Furrow offers supply and delivery of fresh bedding as well as removal of waste bedding. Let us deliver you a container of fresh straw and haul your waste bedding away. A full service solution that is sustainable and responsible.</p>
</article>

<section class="features">
  <div class="feature" style="left:110px">
    <svg width="46" height="66" viewBox="0 0 46 66" fill="none" stroke="#f7941d" stroke-width="2"><circle cx="23" cy="23" r="20"/><circle cx="23" cy="23" r="13"/><path d="M23 15l2.5 5 5.5.8-4 3.9 1 5.5-5-2.6-5 2.6 1-5.5-4-3.9 5.5-.8z"/><path d="M12 40l-6 22 8-5 4 7 5-20M34 40l6 22-8-5-4 7-5-20"/></svg>
    <div><h4>QUALITY<br>GUARANTEED</h4><p>Grown for quality - 100% natural with no<br>chemicals or additives</p></div>
  </div>
  <div class="divider" style="left:430px"></div>
  <div class="feature" style="left:460px">
    <svg width="52" height="56" viewBox="0 0 52 56" fill="none" stroke="#f7941d" stroke-width="2.4"><path d="M10 8 Q2 30 14 46 Q26 56 38 46 Q50 30 42 8"/><path d="M18 22l16 16M34 22L18 38"/></svg>
    <div><h4>FULL SERVICE<br>SOLUTION</h4><p>Dedicated in providing a full service solution<br>of bedding supply &amp; waste removal</p></div>
  </div>
  <div class="divider" style="left:800px"></div>
  <div class="feature" style="left:820px">
    <svg width="60" height="64" viewBox="0 0 60 64" fill="none" stroke="#f7941d" stroke-width="2"><circle cx="30" cy="8" r="5"/><path d="M8 34c0-10 10-17 22-17s22 7 22 17c0 7-4 11-8 13v8h-7v-5h-14v5h-7v-8c-4-2-8-6-8-13z"/><path d="M2 30l6 2"/><circle cx="42" cy="30" r="1.5"/></svg>
    <div><h4>CONVENIENT &amp; COST<br>EFFECTIVE</h4><p>Compressed bags , pellets or bulk products<br>saving in shipping costs</p></div>
  </div>
</section>

<section class="bedding">
  <h2 class="section-title" style="left:0;width:1200px;text-align:center;top:1565px">BEDDING</h2>
  <div class="bed-photo" role="img" aria-label="Horse lying down on a bed of chopped straw"></div>

  <svg class="abs" style="left:360px;top:1680px" width="480" height="460" viewBox="0 0 480 460" fill="none" stroke="#9a9a9a" stroke-width="1.6">
    <path d="M85 52 Q70 32 25 40 M25 40l10-7M25 40l10 7"/>
    <path d="M60 240 Q70 262 20 250 M20 250l8-8M20 250l9 6"/>
    <path d="M150 322 Q130 355 82 355 M82 355l8-8M82 355l9 6"/>
    <path d="M240 340 V392 M240 392l-6-8M240 392l6-8"/>
    <path d="M315 322 Q345 352 382 345 M382 345l-10-7M382 345l-8 8"/>
    <path d="M410 240 Q420 262 470 250 M470 250l-9-7M470 250l-8 8"/>
    <path d="M400 52 Q410 32 460 38 M460 38l-10-7M460 38l-9 8"/>
  </svg>

  <div class="ico o" style="left:284px;top:1674px"><svg viewBox="0 0 38 38"><path d="M19 4c8 6 10 16 0 28C9 20 11 10 19 4z"/><path d="M19 8v28M19 16l-5-4M19 16l5-4M19 23l-6-4M19 23l6-4"/></svg></div>
  <div class="ico-label" style="left:155px;top:1694px;text-align:right;width:114px">100% Natural<br>Chopped Straw</div>

  <div class="ico b" style="left:302px;top:1848px"><svg viewBox="0 0 38 38"><circle cx="19" cy="19" r="14"/><path d="M9 9l20 20"/></svg></div>
  <div class="ico-label" style="left:200px;top:1876px;text-align:right;width:86px">Low Dust</div>

  <div class="ico o" style="left:365px;top:2017px"><svg viewBox="0 0 38 38"><circle cx="19" cy="19" r="14"/><path d="M16 10h6M17 10v8l-6 10h16l-6-10v-8"/></svg></div>
  <div class="ico-label" style="left:240px;top:2033px;text-align:right;width:112px">Chemical &amp;<br>Additive Free</div>

  <div class="ico o" style="left:842px;top:1674px"><svg viewBox="0 0 38 38"><path d="M19 6l6 10h-12zM8 28l6-10 6 10zM30 28l-6-10-6 10z"/></svg></div>
  <div class="ico-label" style="left:934px;top:1694px;width:200px">Environmentally Friendly –<br>Recyclable &amp; Compostable</div>

  <div class="ico b" style="left:817px;top:1848px"><svg viewBox="0 0 38 38"><circle cx="19" cy="19" r="14"/><path d="M10 12c4 0 6 3 5 6s3 4 2 8M24 8c-1 4 3 5 6 5M23 24c2-2 5-1 6 2"/></svg></div>
  <div class="ico-label" style="left:905px;top:1866px;width:200px">Economic – less used<br>and less wasted</div>

  <div class="ico o" style="left:752px;top:2017px"><svg viewBox="0 0 38 38"><path d="M5 26h28v-5l-6-4H12l-7 5zM13 17l3-6h6l3 6M9 26v3M29 26v3"/></svg></div>
  <div class="ico-label" style="left:839px;top:2033px;width:140px">Cheaper than<br>Wood Shavings</div>

  <div class="ico b" style="left:563px;top:2098px"><svg viewBox="0 0 38 38"><circle cx="12" cy="22" r="5"/><circle cx="22" cy="14" r="4"/><circle cx="24" cy="26" r="6"/><circle cx="12" cy="9" r="2"/><path d="M29 8l2 2M29 10l2-2"/></svg></div>
  <div class="ico-label" style="left:500px;top:2180px;width:203px;text-align:center">Clean &amp; Highly<br>Absorbent</div>

  <a class="btn btn-dark view-bed">VIEW BEDDING ›</a>
</section>

<section class="feed">
  <h2>OUR FEED</h2>
  <p class="feed-intro">Hay cubes and pellets are made from premium hay offering a variety of animals a feed that is non-GMO and packed with natural nutrients. These pellets and cubes are less bulky to handle, store and ship. As well, they reduce the amount of wasted feed.</p>

  <div class="feed-item" style="left:118px;top:258px"><svg viewBox="0 0 32 32"><path d="M16 3c7 5 8 14 0 24C8 17 9 8 16 3zM16 8v22"/></svg>100% Natural</div>
  <div class="feed-item" style="left:292px;top:258px"><svg viewBox="0 0 32 32"><circle cx="16" cy="16" r="13"/><path d="M13 8h6M14 8v7l-5 9h14l-5-9V8"/></svg>Chemical &amp;<br>Additive Free</div>
  <div class="feed-item" style="left:442px;top:258px"><svg viewBox="0 0 32 32"><path d="M4 14l7-4 7 4v8l-7 4-7-4zM14 10l7-4 7 4v8l-7 4"/></svg>Available in<br>Pellets or Cubes</div>

  <div class="feed-item" style="left:115px;top:332px"><svg viewBox="0 0 32 32"><circle cx="9" cy="20" r="5"/><circle cx="19" cy="12" r="4"/><circle cx="21" cy="24" r="5"/><path d="M26 6l3 3M26 9l3-3"/></svg>Clean - Eliminates<br>Dust From Feeding<br>Baled Hay</div>
  <div class="feed-item" style="left:292px;top:330px"><svg viewBox="0 0 32 32"><path d="M6 8h20M12 8V5h8v3M8 8l2 20h12l2-20M13 12v12M16 12v12M19 12v12"/></svg>Eliminate Waste<br>In Feeding</div>
  <div class="feed-item" style="left:445px;top:332px"><svg viewBox="0 0 32 32"><path d="M4 18c4-10 20-10 24 0M4 18c4 6 20 6 24 0M10 14l12 8M14 12l10 6"/></svg>High Protein<br>Content</div>

  <div class="feed-item" style="left:112px;top:402px"><svg viewBox="0 0 32 32"><circle cx="14" cy="14" r="11"/><path d="M17 10c-1-2-6-2-6 1s6 2 6 5-5 3-6 1M14 7v2M14 19v2"/><circle cx="25" cy="25" r="4"/></svg>Cost Effective</div>
  <div class="feed-item" style="left:290px;top:402px"><svg viewBox="0 0 32 32"><path d="M28 10A13 13 0 1 1 22 5M10 16l5 5L29 6"/></svg>Convenient</div>
  <div class="feed-item" style="left:448px;top:402px"><svg viewBox="0 0 32 32"><path d="M16 4l6 10H10zM5 26l6-10 6 10zM27 26l-6-10-6 10z"/></svg>Less wasted<br>feed</div>

  <a class="btn view-feed">VIEW FEED ›</a>

  <div class="feed-photo-main" role="img" aria-label="Man feeding a horse from a bucket over a stable gate"></div>
  <div class="feed-photo-pellets" role="img" aria-label="Close-up of hay feed pellets"></div>
</section>

<section class="delivery">
  <div class="delivery-photo" role="img" aria-label="Chestnut horse walking across a green pasture"></div>
  <h2>DELIVERY IN CANADA &amp; USA</h2>
  <div class="delivery-rule"></div>
  <p style="top:3248px">Looking for the best bedding and feed for your horse, livestock or household pet look no further.</p>
  <p style="top:3295px">We use premium locally sourced straw and hay in all of our products and are committed in providing quality products and service.</p>
  <a class="btn contact-btn">CONTACT US</a>
</section>

<footer class="site-footer">
  <svg class="footer-bg" viewBox="0 0 1200 498" preserveAspectRatio="none"><path d="M0 20 Q600 120 1200 20 L1200 498 L0 498Z" fill="#3d2314"/></svg>
  <div class="footer-brand">
    <div class="dot"></div>
    <div class="name">GOLDEN FURROW</div>
    <div class="tag">BEDDING &amp; FEED</div>
  </div>
  <div class="socials"><span></span><span></span><span></span><span></span></div>

  <div class="f-col abs" style="left:427px;top:172px">
    <h5>SITEMAP</h5>
    <ul><li>Home</li><li>About Us</li><li>Our Bedding</li><li>Feed</li><li>Contact Us</li></ul>
  </div>
  <div class="f-col f-contact abs" style="left:602px;top:172px">
    <h5>CONTACT US</h5>
    <ul>
      <li><svg viewBox="0 0 14 14"><path d="M7 1a4.5 4.5 0 0 1 4.5 4.5C11.5 9 7 13 7 13S2.5 9 2.5 5.5A4.5 4.5 0 0 1 7 1z" fill="#f7941d"/><circle cx="7" cy="5.5" r="1.6" fill="#3d2314"/></svg><span>48 Meadow Lane, Fieldtown<br>30417, United States</span></li>
      <li><svg viewBox="0 0 14 14"><path d="M3 1l2.5 3-1.5 1.5c1 2 2.5 3.5 4.5 4.5L10 8.5 13 11l-2 2C6 12 2 8 1 3z" fill="#f7941d"/></svg>(555) 014-2290</li>
      <li style="margin-top:10px"><svg viewBox="0 0 14 14"><rect x="1" y="3" width="12" height="8" fill="#f7941d"/><path d="M1 3l6 5 6-5" stroke="#3d2314" fill="none"/></svg>hello@goldenfurrow.example</li>
    </ul>
  </div>
  <div class="f-col abs" style="left:865px;top:168px">
    <h5>NEWSLETTER SIGN UP</h5>
    <div class="email-field">Email address</div>
    <a class="btn subscribe">SUBSCRIBE</a>
  </div>
  <div class="copyright">© Copyright 2020 . Golden Furrow . All Right Reserved</div>
</footer>

</body>
</html>
```